Author needs a book cover design for a science fiction novel

My name is Peter Dalworth. I need a book cover design for my science fiction novel - "Fair Wind Tovan"
In the 36th century a giant comet is hurtling through space on a collision course with Earth. On its way past Pluto the people of Pluto decide to offer a message of encouragement. They place a huge sign on the comet - FAIR WIND TOVAN in huge red neon letters. (The words FAIR WIND are on top of the word EARTH). So the first thing I need on my cover is the comet with the Fair Wind Tovan sign.
A woman from a time well beyond the 36th century then makes an appearance. She has put the comet on a collision course with Earth in order to protect her own timeline. Her character is an ode to the Sirens of Greek mythology who use their great beauty to lure sailors to their death. She has red hair with a hint of metallic blue, hypnotic blue eyes with a swirl of green, effervescent red lips, a tattoo on her left cheekbone of six blue doves flying in a circle, a short golden dress that shows plenty of cleavage, an Egyption style large golden collar necklace, sandals with leather straps that wind up her calves, fingernails that pulse through the colours of the rainbow in arcs of colour that jump from fingernail to fingernail. So the second thing I need on the cover is a representation of this woman. Prehaps just her face with a wicked smile looking over the comet, but I am open to any variation of the comet and the woman. Done well I think it would make for a very striking book cover.

I would also like PETER DALWORTH written along the bottom of the cover, along with PETER DALWORTH and FAIR WIND TOVAN on the side.

On the Back cover the following blurb:

The unlikely hero:
In 1984 sixteen year old Ramsey follows the advice of a mysterious stranger and sneaks a note into a time capsule that is to be buried at his school. The note is a request to be taken to the future once time travel has been developed. Years later, just when his mundane life is about to come to a sudden and premature end, the prophesy of the note is fulfilled and he finds himself rescued and catapulted into a future world beyond his imagination. He is a man out of his time and out of his depth, but even so he finds that the fate of the human race rests in his hands.

The rescuer:
Tove is a time traveller from the 36th century tasked to rescue Ramsey. To Tove’s horror when he arrives back in the 36th century with Ramsey he finds the timeline in ruins and his world populated by a strange alternative civilisation. Tove and Ramsey zip about through time in an attempt to unravel the mystery only to find the more they dabble with time the worse things become.

The Siren:
She’s wickedly beautiful, dangerous to mess with and from an unknown time eons into the future. She puts a giant comet on a collision course with 36th century Earth. Just what she is up to is a mystery that seems impossible to solve, anyone who looks into her hypnotic blue eyes instantly turns into a love struck idiot. Ramsey thinks that he is strong enough to take her on, but is she really such a big player in the game? Or just a diversionary tactic controlled by a higher power?

Brief updated with better guidelines for what is required.

Clarification on the sign: The sign is flat and sticks to the comet like a stamp. The people of pluto built the sign in space in the path of the comet, the comet ran into it, the sign stuck to the comet. The comet is round and 11 km in diameter. The sign takes up most of the face of the comet, with FAIR WIND written on top of EARTH. The sign is tranparent apart from the letters, which are neon red.

Does anyone need more time?

Target Market(s)

Science fiction fans, the story is not hardcore sci-fi. It is a light hearted romp through time with plenty of humour. I am aiming to release as an eBook and possibly a paper version as well. Size of front cover 6" x 9"

Industry/Entity Type

Tattoo

Colors

Designer to choose colors to be used in the design.

Requirements
Must have
• Comet on the front cover with FAIRS WIND TOVAN sign written on it in large neon letters. The words FAIR WIND on top and EARTH below. The sign takes up most of the space on the face of the comet.
The woman as described earlier, must be very attractive with a wicked smile. Either her face above the comet, or whole body, perhaps beckoning the comet towards the Earth with her rainbow fingers. Or some other combination of the comet and woman that looks good. I would like her to look sexy, imposing and classy, not cheesy or sleazy.
Nice to have
• Prefer that the woman have red hair with a hint of metallic blue, but if you think another colour looks better go with it and I can change her hair colour in the book to match. Change her golden dress too if another outfit looks better.
Should not have
• Fair Wind Tovan in small writing, woman who doesn't look stunning. Gold collar necklace shouldn't be so big as to be a distraction.
I want people to look at the cover and think, wow this looks interesting, and who is she?

```html
<!DOCTYPE html>
<html lang="en">
<head>
<meta charset="utf-8">
<title>Fair Wind Tovan – Book Cover</title>
<link rel="stylesheet" href="https://fonts.googleapis.com/css2?family=Oswald:wght@500;600;700&family=Roboto+Condensed:wght@400;500;700&display=swap">
<style>
  :root {
    --page: #e9e9ea;
    --ink-black: #0b0b0c;
    --back-title: #cfcfcf;
    --blurb-text: #e6e6e6;
    --neon-red: #ff2b2b;
    --neon-core: #ffe3e3;
    --art-deep: #1a1d44;
    --art-warm: #d9631f;
    --art-glow: #f2b040;
    --author-dark: #151515;
  }
  * { margin: 0; padding: 0; box-sizing: border-box; }
  html, body {
    width: 1200px; height: 800px; overflow: hidden;
    background: var(--page);
  }
  .cover-spread {
    position: absolute;
    left: 178px; top: 100px;
    width: 844px; height: 600px;
    display: flex;
    box-shadow: 0 14px 30px rgba(0,0,0,.22);
  }

  /* Back cover */
  .back-cover {
    width: 400px; height: 600px;
    background: var(--ink-black);
    padding: 30px 34px 24px;
    display: flex; flex-direction: column;
    color: var(--blurb-text);
  }
  .back-author {
    align-self: flex-end;
    font-family: "Oswald", sans-serif;
    font-weight: 600; font-size: 12px; letter-spacing: .5px;
    color: var(--back-title);
    margin-right: 20px;
  }
  .back-title {
    font-family: "Oswald", sans-serif;
    font-weight: 700; font-size: 40px; line-height: 1;
    color: var(--back-title);
    text-align: center;
    margin: 2px 0 18px;
  }
  .blurb-heading {
    font-family: "Roboto Condensed", sans-serif;
    font-weight: 700; font-size: 10px;
    text-align: center; text-transform: uppercase;
    margin: 10px 0 1px;
  }
  .blurb-text {
    font-family: "Roboto Condensed", sans-serif;
    font-weight: 500;
    font-size: 9.6px; line-height: 1.34;
    text-align: justify; text-align-last: center;
  }
  .back-footer {
    margin-top: auto;
    font-family: "Roboto Condensed", sans-serif;
    font-size: 7px; letter-spacing: .5px;
    padding-left: 60px;
  }

  /* Spine */
  .spine {
    width: 44px; height: 600px;
    background: var(--ink-black);
    display: flex; flex-direction: column; align-items: center;
    padding: 22px 0;
  }
  .spine-title, .spine-author {
    writing-mode: vertical-rl;
    font-family: "Oswald", sans-serif;
    color: #f0f0f0;
  }
  .spine-title { font-weight: 600; font-size: 24px; letter-spacing: 9px; }
  .spine-author { font-weight: 500; font-size: 8px; letter-spacing: 1.5px; margin-top: 40px; }

  /* Front cover */
  .front-cover {
    position: relative;
    width: 400px; height: 600px;
    overflow: hidden;
  }
  .cover-art-placeholder {
    position: absolute; inset: 0;
    background: linear-gradient(155deg, var(--art-warm) 0%, var(--art-deep) 50%, var(--art-glow) 100%);
  }
  .front-title {
    position: absolute; left: 0; right: 0; top: 28px;
    text-align: center;
    font-family: "Oswald", sans-serif;
    font-weight: 700; font-size: 104px; line-height: .98;
    letter-spacing: 2px;
    color: rgba(255, 43, 43, .85);
    -webkit-text-stroke: 2.5px var(--neon-core);
    text-shadow:
      0 0 4px var(--neon-red),
      0 0 10px var(--neon-red),
      0 0 22px var(--neon-red);
  }
  .front-title span { display: block; }
  .front-author {
    position: absolute; left: 0; right: 0; bottom: 18px;
    text-align: center;
    font-family: "Oswald", sans-serif;
    font-weight: 700; font-size: 26px; letter-spacing: 1px;
    color: var(--author-dark);
  }
</style>
</head>
<body>
  <main class="cover-spread">
    <section class="back-cover">
      <p class="back-author">PETER DALWORTH</p>
      <h2 class="back-title">FAIR WIND TOVAN</h2>

      <h3 class="blurb-heading">The unlikely hero:</h3>
      <p class="blurb-text">In 1984 sixteen year old Ramsey follows the advice of a mysterious stranger and sneaks a note into a time capsule that is to be buried at his school. The note is a request to be taken to the future once time travel has been developed. Years later, just when his mundane life is about to come to a sudden and premature end, the prophesy of the note is fulfilled and he finds himself rescued and catapulted into a future world beyond his imagination. He is a man out of his time and out of his depth, but even so he finds that the fate of the human race rests in his hands.</p>

      <h3 class="blurb-heading">The rescuer:</h3>
      <p class="blurb-text">Tove is a time traveller from the 36th century tasked to rescue Ramsey. To Tove’s horror when he arrives back in the 36th century with Ramsey he finds the timeline in ruins and his world populated by a strange alternative civilisation. Tove and Ramsey zip about through time in an attempt to unravel the mystery only to find the more they dabble with time the worse things become.</p>

      <h3 class="blurb-heading">The Siren:</h3>
      <p class="blurb-text">She’s wickedly beautiful, dangerous to mess with and from an unknown time eons into the future. She puts a giant comet on a collision course with 36th century Earth. Just what she is up to is a mystery that seems impossible to solve, anyone who looks into her hypnotic blue eyes instantly turns into a love struck idiot. Ramsey thinks that he is strong enough to take her on, but is she really such a big player in the game? Or just a diversionary tactic controlled by a higher power?</p>

      <p class="back-footer">ISBN</p>
    </section>

    <aside class="spine">
      <p class="spine-title">FAIR WIND TOVAN</p>
      <p class="spine-author">PETER DALWORTH</p>
    </aside>

    <section class="front-cover">
      <div class="cover-art-placeholder" role="img" aria-label="Cover illustration: a fiery solar burst over the edge of a glowing planet in deep space"></div>
      <h1 class="front-title"><span>FAIR</span><span>WIND</span><span>TOVAN</span></h1>
      <p class="front-author">PETER DALWORTH</p>
    </section>
  </main>
</body>
</html>
```